Kestrel Bridge Consulting (KBC) Business Card Design

I would like to create double-sided business cards that contain:
1) Name: Derek Molvane
2) Phone Number: +1 (555) 218-4907
3) Email: Derek.Molvane@KestrelBridgeConsulting.example
4) Website: KestrelBridgeConsulting.example

I would like to include my logo and a color scheme similar to the Varnholt Grand Prix Ostera squad color scheme (black, silver, greenish-blue – but can also include regular blue)

What we do: Our company develops and delivers innovative and pragmatic information technology and cybersecurity risk and compliance solutions for organizations in the commercial market as well as the federal, and state/local sectors.

```html
<!DOCTYPE html>
<html lang="en">
<head>
<meta charset="utf-8">
<title>Kestrel Bridge Consulting – Business Card</title>
<link rel="stylesheet" href="https://fonts.googleapis.com/css2?family=Jost:wght@400;500&family=Michroma&display=swap">
<style>
  :root {
    --stage-top: #05bfb0;
    --stage-bottom: #02978b;
    --card-dark-1: #0b4f52;
    --card-dark-2: #052f30;
    --teal: #1bb5a3;
    --teal-deep: #0f8f86;
    --circuit-light: #9adfd6;
    --ink: #111517;
    --white: #ffffff;
  }
  * { margin: 0; padding: 0; box-sizing: border-box; }
  html, body {
    width: 1043px;
    height: 1200px;
    overflow: hidden;
  }
  body {
    position: relative;
    background: linear-gradient(180deg, var(--stage-top) 0%, var(--stage-bottom) 100%);
    font-family: "Jost", "Helvetica Neue", Arial, sans-serif;
  }
  .card {
    position: absolute;
    left: 172px;
    width: 700px;
    overflow: hidden;
  }
  /* Front */
  .card--front {
    top: 154px;
    height: 400px;
    background: linear-gradient(100deg, var(--card-dark-1) 0%, #083e40 50%, var(--card-dark-2) 100%);
  }
  .card--front .circuit-art {
    position: absolute;
    left: 0; top: 0;
    width: 330px; height: 400px;
    background:
      radial-gradient(circle at 20% 70%, rgba(40, 200, 180, 0.35), transparent 45%),
      radial-gradient(circle at 45% 25%, rgba(30, 150, 170, 0.25), transparent 50%),
      linear-gradient(90deg, rgba(20, 120, 140, 0.35), transparent);
  }
  .brand {
    position: absolute;
    left: 162px;
    top: 152px;
    display: flex;
    align-items: center;
    gap: 18px;
  }
  .brand__mark {
    width: 78px;
    height: 78px;
    border-radius: 50%;
    background: var(--teal);
  }
  .brand__name {
    color: var(--white);
    font-weight: 500;
    font-size: 27px;
    line-height: 28px;
    letter-spacing: 1px;
    text-transform: uppercase;
  }
  /* Back */
  .card--back {
    top: 647px;
    height: 402px;
    background: var(--white);
  }
  .card--back .circuit-art {
    position: absolute;
    left: 0; top: 0;
    width: 260px; height: 402px;
    background: linear-gradient(90deg, rgba(154, 223, 214, 0.55) 0%, rgba(154, 223, 214, 0.25) 65%, rgba(255, 255, 255, 0) 100%);
  }
  .divider {
    position: absolute;
    left: 246px;
    top: 88px;
    width: 2px;
    height: 222px;
    background: var(--ink);
  }
  .person-name {
    position: absolute;
    left: 274px;
    top: 88px;
    font-family: "Michroma", "Arial Black", sans-serif;
    font-size: 19px;
    letter-spacing: 1px;
    text-transform: uppercase;
    background: linear-gradient(90deg, var(--teal), var(--teal-deep));
    -webkit-background-clip: text;
    background-clip: text;
    color: transparent;
  }
  .contacts {
    position: absolute;
    left: 216px;
    top: 180px;
    list-style: none;
  }
  .contact {
    display: flex;
    align-items: center;
    height: 40px;
    color: var(--ink);
    font-size: 18.5px;
  }
  .contact__icon {
    width: 17px;
    height: 17px;
    border-radius: 50%;
    background: var(--teal-deep);
    margin-right: 37px;
    display: flex;
    align-items: center;
    justify-content: center;
  }
  .contact__icon svg { width: 10px; height: 10px; }
</style>
</head>
<body>
  <section class="card card--front" aria-label="Business card front">
    <div class="circuit-art" role="img" aria-label="Glowing teal circuit-board pattern"></div>
    <div class="brand">
      <span class="brand__mark" aria-hidden="true"></span>
      <span class="brand__name">Kestrel<br>Bridge<br>Consulting</span>
    </div>
  </section>

  <section class="card card--back" aria-label="Business card back">
    <div class="circuit-art" role="img" aria-label="Light teal circuit-board pattern"></div>
    <div class="divider"></div>
    <h1 class="person-name">Derek Molvane</h1>
    <ul class="contacts">
      <li class="contact">
        <span class="contact__icon">
          <svg viewBox="0 0 10 10"><path d="M2.2 1 L3.6 1 L4.2 3 L3.2 3.8 Q4 5.8 6.2 6.8 L7 5.8 L9 6.4 L9 7.8 Q8.6 9 7.4 9 Q1 8.2 1 2.4 Q1 1.2 2.2 1 Z" fill="#fff"/></svg>
        </span>
        +1 (555) 218-4907
      </li>
      <li class="contact">
        <span class="contact__icon">
          <svg viewBox="0 0 10 10"><rect x="1" y="2.5" width="8" height="5.5" fill="#fff"/><path d="M1 2.5 L5 5.6 L9 2.5" stroke="#0f8f86" stroke-width="0.9" fill="none"/></svg>
        </span>
        Derek.Molvane@KestrelBridgeConsulting.example
      </li>
      <li class="contact">
        <span class="contact__icon">
          <svg viewBox="0 0 10 10" fill="none" stroke="#fff" stroke-width="0.9"><circle cx="5" cy="5" r="3.8"/><ellipse cx="5" cy="5" rx="1.6" ry="3.8"/><path d="M1.2 5 H8.8"/></svg>
        </span>
        KestrelBridgeConsulting.example
      </li>
    </ul>
  </section>
</body>
</html>
```